Design Website Templates for Photographers for Lumora Inc. (trywendle.com)

Lumora Inc. is a generative website company for wedding photographers.
We are seeking new photography website design inspirations for the next template to be offered on our platform. The catch is you must use the same data for your designs. You also must use all of the data somewhere in the design. You cannot add new content besides the data available. If you wish to add any elements It will be hardcoded and must be universally fitting for many different photographers. We recommend not using any hardcoded test.
Don't be afraid to be creative! Although the most important element of a photographers website is the photos, we are looking for unique and out-of-the-box designs for the actual site as well.
Here is the User generated data available to you:
- 4 Hero Images Landscape, 4 Hero Images Portrait
- Tagline “destination photographer based in Maui, Hawaii”
- “About Photo” of the photographer
- “About” Biography Text
- The design can use up to 3 colors + background color and 2 fonts
- 9 Gallery images
- 3 Packages/services that include landscape/portrait images, a price, a title and text
- Testimonials made up of an image, text and text for the name of testimonial giver
See some examples of our current website designs attached. You can use any of the data you see in the designs.
Updates
We are looking for designs that are less feminine and are more neutral in color and fonts. Currently our templates are more oriented towards feminine photographers. We want to have designs that speak to diverse audiences. We thank everyone for submitting and are reviewing the designs.
Number of Pages Required
1 page
Look and feel
Each slider illustrates characteristics of the customer's brand and the style your logo design should communicate.

```html
<!DOCTYPE html>
<html lang="en">
<head>
<meta charset="utf-8">
<title>Lumora — Destination Photographer</title>
<link href="https://fonts.googleapis.com/css2?family=Jost:wght@300;400;500;600;700;800&family=Montserrat:wght@800&display=swap" rel="stylesheet">
<style>
:root{
  --ink:#1d1d1d;
  --night:#1e1e1f;
  --paper:#ffffff;
  --mute:#6f6f6f;
  --gold:#f2b632;
  --line:#d6d6d6;
}
*{margin:0;padding:0;box-sizing:border-box}
html,body{width:1200px;height:4992px;overflow:hidden}
body{font-family:"Jost",sans-serif;color:var(--ink);background:var(--paper);position:relative}
.abs{position:absolute}
.photo{position:absolute}

/* header + hero */
.hero{position:absolute;left:0;top:0;width:1200px;height:603px;
  background:radial-gradient(ellipse at 70% 60%,#4a3f37 0%,#2f2c2a 45%,#232323 100%)}
.logo{position:absolute;font-weight:500;letter-spacing:1px;color:var(--paper)}
.site-logo{left:58px;top:22px;font-size:32px}
.main-nav{position:absolute;left:344px;top:33px;display:flex;gap:0;font-size:11px;color:var(--paper);text-transform:uppercase}
.main-nav span{position:absolute;white-space:nowrap}
.book-btn{position:absolute;left:1012px;top:23px;width:130px;height:35px;border:1px solid var(--paper);color:var(--paper);
  font-size:11px;display:flex;align-items:center;justify-content:center;text-transform:uppercase}
.hero-title{position:absolute;left:147px;top:184px;font-family:"Montserrat",sans-serif;font-weight:800;color:var(--paper);
  font-size:50px;line-height:51px;text-transform:uppercase;letter-spacing:-.5px}
.hero-link{position:absolute;left:150px;top:410px;font-size:11px;color:var(--paper);text-transform:uppercase}
.scroll-cue{position:absolute;left:1092px;top:372px}

/* intro */
.intro{position:absolute;left:223px;top:682px;width:470px;font-size:16.5px;font-weight:600;line-height:22px;text-transform:uppercase}

/* services grid */
.service-label{position:absolute;font-size:21px;letter-spacing:6px;font-weight:400;text-transform:uppercase}
.rule{position:absolute;height:1px;background:#555}

/* about */
.section-title{position:absolute;font-weight:500;font-size:43px;text-transform:uppercase;letter-spacing:.5px}
.body-copy{position:absolute;font-size:12.5px;line-height:21.5px;color:#555;font-weight:300}

/* gallery */
.caption{position:absolute;font-size:13px;color:#777;font-weight:300}
.dark-band{position:absolute;left:0;top:2694px;width:1200px;height:2298px;background:var(--night)}
.dark .caption{color:#aaa}

/* cta */
.cta{position:absolute;top:3330px;width:450px;height:300px;border:1px solid #cfcfcf;color:var(--paper);text-align:center}
.cta h3{font-weight:400;font-size:28px;line-height:34px;position:absolute;left:0;width:100%}
.cta .btn{position:absolute;left:50%;transform:translateX(-50%);background:var(--gold);color:var(--paper);font-size:10.5px;font-weight:600;
  padding:0 18px;height:34px;line-height:34px;text-transform:uppercase;white-space:nowrap}
.cta .lead{position:absolute;left:40px;right:40px;font-size:15px;line-height:25px}
.cta .list{position:absolute;left:50px;right:50px;font-size:12px;line-height:22px;color:#cfcfcf;font-weight:300}

/* testimonials */
.on-dark{color:var(--paper)}
.quote{position:absolute;left:611px;width:420px;font-size:12px;line-height:21.5px;color:#cfcfcf;font-weight:300}
.quote b{display:block;margin-top:8px;color:var(--paper);font-weight:400}

/* link tiles */
.tiles{position:absolute;left:149px;top:4192px;width:900px;height:122px;border:1px solid #cfcfcf;display:flex}
.tile{flex:1;border-right:1px solid #cfcfcf;color:var(--paper);text-align:center;padding-top:36px}
.tile:last-child{border-right:0}
.tile small{display:block;font-size:10px;text-transform:uppercase;margin-bottom:2px}
.tile strong{font-weight:400;font-size:29px;text-transform:uppercase}

/* contact */
.field{position:absolute;left:611px;font-size:17px;color:var(--paper)}
.send{position:absolute;left:611px;top:4746px;width:131px;height:37px;border:1px solid #cfcfcf;color:var(--paper);font-size:10.5px;
  display:flex;align-items:center;justify-content:center;text-transform:uppercase}

/* footer */
.foot{position:absolute;font-size:11.5px;line-height:27px;color:#cfcfcf;font-weight:300}
.social{position:absolute;left:895px;top:4917px;display:flex;gap:10px}
.social i{width:13px;height:13px;border-radius:50%;background:var(--paper);display:block}
</style>
</head>
<body>

<!-- Hero -->
<section class="hero" role="img" aria-label="Dimly lit lifestyle photograph as hero background">
</section>
<div class="logo site-logo">LUMORA</div>
<nav class="main-nav">
  <span style="left:0">About</span>
  <span style="left:92px">Blog</span>
  <span style="left:174px">Testimonials</span>
  <span style="left:310px">Portfolio</span>
  <span style="left:427px">Get in touch</span>
</nav>
<div class="book-btn">Book with me</div>
<h1 class="hero-title">Destination<br>photographer<br>based in<br>Maui, Hawaii</h1>
<div class="hero-link">View projects</div>
<svg class="scroll-cue" width="20" height="130" viewBox="0 0 20 130" aria-hidden="true">
  <polyline points="6,8 10,4 14,8" fill="none" stroke="#fff" stroke-width="1.5"/>
  <line x1="10" y1="32" x2="10" y2="90" stroke="#fff" stroke-width="1.5"/>
  <polyline points="6,120 10,124 14,120" fill="none" stroke="#fff" stroke-width="1.5"/>
</svg>

<!-- Intro -->
<p class="intro">Lumora combine the classic knowledge of traditinal photographic and immerse yourself in the mesmerizing world of landscape photography.</p>

<!-- Services -->
<div class="photo" style="left:149px;top:847px;width:198px;height:170px;background:linear-gradient(135deg,#f1ece4,#d9c9b2)" role="img" aria-label="Lifestyle photo: flowers and eggs on a table"></div>
<div class="photo" style="left:347px;top:847px;width:198px;height:170px;background:linear-gradient(180deg,#8fc4e6,#1f5e8c)" role="img" aria-label="Lifestyle photo: person on a boat at sea"></div>
<div class="photo" style="left:545px;top:847px;width:197px;height:170px;background:linear-gradient(135deg,#e6e6e6,#6d6d6d)" role="img" aria-label="Lifestyle photo: person working by a window"></div>
<div class="rule" style="left:149px;top:1017px;width:593px"></div>
<div class="service-label" style="left:795px;top:918px">1. Lifestyle</div>

<div class="service-label" style="left:186px;top:1090px">2. Portraits</div>
<div class="rule" style="left:149px;top:1190px;width:308px"></div>
<div class="photo" style="left:457px;top:1019px;width:197px;height:171px;background:linear-gradient(135deg,#3b2a22,#8a6a55)" role="img" aria-label="Portrait photo with curly hair"></div>
<div class="photo" style="left:654px;top:1019px;width:198px;height:171px;background:linear-gradient(135deg,#2a1a14,#c4552a)" role="img" aria-label="Portrait photo with warm city lights"></div>
<div class="photo" style="left:852px;top:1019px;width:197px;height:171px;background:linear-gradient(135deg,#7a6046,#2f6e4a)" role="img" aria-label="Portrait photo in sunlight"></div>

<div class="photo" style="left:149px;top:1192px;width:198px;height:170px;background:linear-gradient(135deg,#f2f0ea,#8a7f6c)" role="img" aria-label="Commercial photo of product jars"></div>
<div class="photo" style="left:347px;top:1192px;width:198px;height:170px;background:linear-gradient(135deg,#e8c2a8,#b6402c)" role="img" aria-label="Commercial photo of a candle"></div>
<div class="photo" style="left:545px;top:1192px;width:197px;height:170px;background:linear-gradient(135deg,#f1eef3,#a48bc9)" role="img" aria-label="Commercial photo of a makeup palette"></div>
<div class="service-label" style="left:795px;top:1263px">3. Commercial</div>

<!-- About -->
<h2 class="section-title" style="left:223px;top:1512px">About Nell</h2>
<div class="body-copy" style="left:223px;top:1580px;width:475px">
  <p>Immerse yourself in the mesmerizing world of landscape photography. From majestic mountains to serene seascapes, our images showcase the awe-inspiring beauty of nature. Lorem ipsum dolor sit amet consectetur. Duis quis amet nunc vulputate pellentesque massa mi aliquam. Fusce semper aliquam egestas mauris est nunc. Et pellentesque sodales elementum cursus mattis.</p>
  <p style="margin-top:21px">Suscipit etiam nulla odio. Molestie tristique cursus ipsum non vitae nibh amet lacus. Orci dictum erat vitae at at non massa. Sit sit nisl pretium quisque ornare nunc posuere nunc. Erat est varius pulvinar sodales massa pulvinar risus. Orci at ipsum tellus posuere nunc. Auctor malesuada placerat scelerisque est.</p>
</div>
<div class="photo" style="left:766px;top:1442px;width:372px;height:419px;background:linear-gradient(160deg,#f4f1ed,#c8a37e 60%,#8b8b88)" role="img" aria-label="Photo of the photographer in a knit sweater"></div>

<!-- Recent work -->
<div class="dark-band"></div>
<h2 class="section-title" style="left:223px;top:1955px">Recent Work</h2>
<div class="photo" style="left:149px;top:2041px;width:402px;height:374px;background:radial-gradient(circle at 30% 25%,#e6a14a,#3a2f29 45%,#1f1c1b)" role="img" aria-label="Candle with red berries on dark cloth"></div>
<p class="caption" style="left:149px;top:2430px">Cozy at Home Couples Session</p>
<div class="photo" style="left:649px;top:2119px;width:400px;height:445px;background:linear-gradient(180deg,#9fb3c2,#6e7a4c 40%,#8c8a66)" role="img" aria-label="Aerial view of a couple on a country road"></div>
<p class="caption" style="left:649px;top:2581px">Cozy at Home Couples Session</p>
<div class="photo" style="left:149px;top:2496px;width:402px;height:315px;background:linear-gradient(135deg,#e9e7e2,#a9a7a0)" role="img" aria-label="Daisies scattered on white fabric"></div>
<p class="caption" style="left:149px;top:2826px;color:#aaa">Cozy at Home Couples Session</p>
<div class="photo" style="left:649px;top:2653px;width:400px;height:487px;background:linear-gradient(180deg,#9c9a97,#e8b27c 45%,#4a3e36 70%,#1d1b1a)" role="img" aria-label="Couple on a beach at sunset"></div>
<p class="caption" style="left:649px;top:3155px;color:#aaa">Cozy at Home Couples Session</p>
<div class="photo" style="left:149px;top:2892px;width:402px;height:312px;background:linear-gradient(180deg,#c9b9a0,#7d6c5a 60%,#4d4540)" role="img" aria-label="Family walking down a city street"></div>
<p class="caption" style="left:149px;top:3219px;color:#aaa">Cozy at Home Couples Session</p>

<!-- CTA -->
<div class="cta" style="left:149px">
  <h3 style="top:66px">Are you a photographer?</h3>
  <div class="btn" style="top:106px">Get started here</div>
  <p class="lead" style="top:168px">Level the playing field with Lumora.</p>
  <p class="list" style="top:208px">Website * Package * Galleries * Bookings * Payments<br>Contacts * Automated SEO * All-in-One</p>
</div>
<div class="cta" style="left:599px">
  <h3 style="top:48px">Are you looking to book a<br>photographer?</h3>
  <div class="btn" style="top:131px">Visit the marketplace</div>
  <p class="lead" style="top:190px">Browse over 1000+ photographers to find the ferfect match.</p>
  <p class="list" style="top:252px">Weddings * Family * Newborn * Headshots * and More</p>
</div>

<!-- Client love -->
<h2 class="section-title on-dark" style="left:223px;top:3748px;line-height:40px">Client<br>Love</h2>
<p class="body-copy" style="left:226px;top:3840px;width:290px;color:#cfcfcf;font-size:11.5px">Lorem ipsum dolor sit amet consectetur. Duis quis amet nunc vulputate pellentesque.</p>
<div class="quote" style="top:3808px">“We loved our time here at your wonderful studio. A special place with exceptional attention to detail. Lorem ipsum dolor sit amet consectetur. Duis quis amet nunc vulputate pellentesque massa mi aliquam. Fusce semper aliquam egestas mauris est nunc.<b>Ivy Carver, Artist</b></div>
<div class="rule" style="left:611px;top:3942px;width:438px;background:#cfcfcf"></div>
<div class="quote" style="top:3963px">“We loved our time here at your wonderful studio. A special place with exceptional attention to detail. Lorem ipsum dolor sit amet consectetur. Duis quis amet nunc vulputate pellentesque massa mi aliquam. Fusce semper aliquam egestas mauris est nunc.<b>Ivy Carver, Artist</b></div>

<!-- Link tiles -->
<div class="tiles">
  <div class="tile"><small>Info</small><strong>About</strong></div>
  <div class="tile"><small>Our works</small><strong>Portfolio</strong></div>
  <div class="tile"><small>Contact</small><strong>Write us</strong></div>
</div>

<!-- Contact -->
<h2 class="section-title on-dark" style="left:223px;top:4418px;line-height:40px">Let’s<br>Contact</h2>
<p class="body-copy" style="left:226px;top:4512px;width:290px;color:#cfcfcf;font-size:11.5px">Lorem ipsum dolor sit amet consectetur. Duis quis amet nunc vulputate pellentesque.</p>
<div class="field" style="top:4467px">Name</div>
<div class="field" style="top:4546px">Email</div>
<div class="field" style="top:4626px">Message</div>
<div class="rule" style="left:611px;top:4704px;width:438px;background:#cfcfcf"></div>
<div class="send">Send message</div>

<!-- Footer -->
<div class="logo" style="left:149px;top:4860px;font-size:34px">LUMORA</div>
<p class="foot" style="left:149px;top:4911px">© 2023 LUMORA - All Rights Reserved.</p>
<p class="foot" style="left:457px;top:4884px">contact@trywendle.com<br>+1 555 010 4821</p>
<p class="foot" style="left:688px;top:4884px">2250 Harbor Ln, Victoria,<br>BC V0V 1A1</p>
<p class="foot" style="left:895px;top:4884px">Follow my socials:</p>
<div class="social" aria-label="Social links"><i></i><i></i><i></i></div>

</body>
</html>
```